Zanquorra Business Card Design

Zanquorra is a small and new restaurant/ bar location in Hong Kong. The name "Djibouti" derives from an African country. There is no specific reason behind other than the fact, that the bar is somewhat inspired by African elements (only inspired but not purely based on African cuisine etc.).

The bar is somewhat a fusion of African, Mediterranean and Oriental (Old French Vietnam) elements.

However, it is very imperative to stress, that the overall look and feel of Zanquorra is a very high end cocktail lounge/ bar location. The bar is tucked away in a hidden alley, so people will have to know about it. The idea is to send the consumer off in an Escape or hidden remote location where they are at ease in a hip, stylish and trendy environment.

The card needs to feel high-end.

Final logo artwork has been attached and also pictures of the bar/ restaurant itself. The logo ie monkey head cannot be modified. However, the background color and the color of the type "ZANQUORRA" can be changed.

The following details need to fit onto the business card. Of course they can be arranged to your liking:

LOGO

Colin Vey
Partner

+852 97035164
xxx@zanquorra.com
www.zanquorra.com
7C, Brennick Road, Wan Chai, Hong Kong

```html
<!DOCTYPE html>
<html lang="en">
<head>
<meta charset="UTF-8">
<title>Zanquorra Business Card</title>
<link rel="stylesheet" href="https://fonts.googleapis.com/css2?family=Montserrat:wght@400;500;700&display=swap">
<style>
  :root {
    --canvas-bg: #e9e6e2;
    --card-white: #ffffff;
    --ink-black: #1d1d1b;
    --ink-grey: #5c5c5c;
    --accent-red: #c8202a;
    --orange-deep: #e5520f;
    --orange-mid: #f38a12;
    --yellow-bright: #fcc21b;
    --mark-circle: #2a2a2a;
  }
  * { margin: 0; padding: 0; box-sizing: border-box; }
  html, body {
    width: 900px;
    height: 1200px;
    overflow: hidden;
    background: var(--canvas-bg);
    font-family: "Montserrat", sans-serif;
  }
  .card-set {
    position: absolute;
    top: 270px;
    left: 50px;
    display: flex;
    gap: 40px;
  }
  .card {
    width: 380px;
    height: 660px;
    box-shadow: 0 10px 30px rgba(0,0,0,0.18);
  }
  .card-back {
    background: linear-gradient(90deg, var(--orange-deep) 0%, var(--orange-mid) 55%, var(--yellow-bright) 100%);
  }
  .card-front {
    background: var(--card-white);
    display: flex;
    flex-direction: column;
    align-items: center;
    padding-top: 90px;
  }
  .brand-mark {
    width: 120px;
    height: 120px;
    border-radius: 50%;
    background: var(--mark-circle);
  }
  .brand-name {
    margin-top: 26px;
    font-weight: 700;
    font-size: 34px;
    letter-spacing: 3px;
    color: var(--ink-black);
  }
  .contact-block {
    margin-top: 48px;
    width: 230px;
    color: var(--ink-grey);
    font-size: 14px;
    line-height: 1.55;
  }
  .person-name {
    color: var(--accent-red);
    font-weight: 700;
    font-size: 18px;
    letter-spacing: 1.5px;
    text-transform: uppercase;
  }
  .person-role {
    font-size: 13px;
    margin-bottom: 22px;
    color: var(--accent-red);
  }
  .contact-line {
    display: flex;
    align-items: center;
    gap: 8px;
  }
  .contact-line svg { width: 12px; height: 12px; flex: none; }
  .address { margin-top: 14px; }
</style>
</head>
<body>
  <main class="card-set">
    <section class="card card-back" role="img" aria-label="Back of card: repeating pattern of the bar's emblem in circles over an orange to yellow gradient"></section>

    <section class="card card-front">
      <div class="brand-mark"></div>
      <div class="brand-name">ZANQUORRA</div>

      <div class="contact-block">
        <div class="person-name">Colin Vey</div>
        <div class="person-role">Partner</div>

        <div class="contact-line">
          <svg viewBox="0 0 12 12"><path d="M2.5 1 L4.5 1 L5.2 3.5 L4 4.5 Q5 6.8 7.5 8 L8.5 6.8 L11 7.5 L11 9.5 Q10.5 11 9 11 Q1 10 1 3 Q1 1.5 2.5 1 Z" fill="#5c5c5c"/></svg>
          <span>+852 97035164</span>
        </div>
        <div class="contact-line">
          <svg viewBox="0 0 12 12"><rect x="1" y="2.5" width="10" height="7" fill="none" stroke="#5c5c5c" stroke-width="1.2"/><path d="M1 2.5 L6 6.5 L11 2.5" fill="none" stroke="#5c5c5c" stroke-width="1.2"/></svg>
          <span>xxx@zanquorra.com</span>
        </div>
        <div class="contact-line">
          <svg viewBox="0 0 12 12"><circle cx="6" cy="6" r="5" fill="none" stroke="#5c5c5c" stroke-width="1.2"/><path d="M1 6 H11 M6 1 Q3 6 6 11 M6 1 Q9 6 6 11" fill="none" stroke="#5c5c5c" stroke-width="1"/></svg>
          <span>www.zanquorra.com</span>
        </div>
        <div class="address">7C, Brennick Road<br>Wan Chai, Hong Kong</div>
      </div>
    </section>
  </main>
</body>
</html>
```